Marlowe Bay Consulting Business Card

Hi Corvel. Thank you for your work on my coaching business card. I have another business which needs a new card. It is my counselling business. The best way to find out how to approach this project will be to go to my other website. www.marlowebayconsulting.com.au and you will be able to see the colours scheme that I will require. White, Green and blue.

The tag line is Marlowe Bay Consulting So you can look forward to tomorrow. The clients are varied but mostly middle class Australian. The card is to show on it the same details as my other business card but with a different phone number. The tag lines are obviously different. The phone number is 9137 5264 The addresses are all the same.

Again simple, professional sophisticated is best.

```html
<!DOCTYPE html>
<html lang="en">
<head>
<meta charset="utf-8">
<title>Marlowe Bay Consulting Business Card</title>
<link href="https://fonts.googleapis.com/css2?family=Marcellus&family=Open+Sans:wght@300;400;600&display=swap" rel="stylesheet">
<style>
  :root {
    --bg: #e9e9e7;
    --card: #ffffff;
    --blue: #6f9fd8;
    --blue-soft: #8fb1d9;
    --green: #86c440;
    --ink: #1f1f1f;
    --ink-soft: #3a3a3a;
  }
  * { box-sizing: border-box; margin: 0; padding: 0; }
  html, body { width: 1200px; height: 803px; overflow: hidden; background: var(--bg); }
  .stage { position: relative; width: 1200px; height: 803px; }
  .card {
    position: absolute; top: 238px; width: 530px; height: 324px;
    background: var(--card); box-shadow: 0 6px 18px rgba(0,0,0,.12);
    overflow: hidden;
  }
  .card--front { left: 40px; }
  .card--back { left: 630px; }

  .brand-name { font-family: "Marcellus", serif; color: var(--blue); font-weight: 400; letter-spacing: .3px; white-space: nowrap; }
  .tagline { font-family: "Open Sans", sans-serif; text-transform: uppercase; white-space: nowrap; }

  /* front */
  .card--front .brand-name { position: absolute; left: 34px; top: 44px; font-size: 38px; }
  .card--front .rule { position: absolute; left: 34px; top: 100px; width: 462px; height: 2px; background: var(--green); }
  .card--front .tagline { position: absolute; left: 34px; top: 112px; font-size: 17px; font-weight: 300; color: var(--blue-soft); line-height: 1.4; letter-spacing: .5px; }
  .services { position: absolute; left: 34px; bottom: 34px; font-family: "Open Sans", sans-serif; font-size: 15px; color: var(--blue); line-height: 1.5; white-space: nowrap; }
  .services .dot { color: var(--green); padding: 0 4px; }

  /* back */
  .card--back .brand-name { position: absolute; left: 24px; top: 26px; font-size: 23px; }
  .card--back .tagline { position: absolute; left: 24px; top: 60px; font-size: 9px; color: var(--green); line-height: 1.4; }
  .person { position: absolute; right: 24px; top: 28px; text-align: right; font-family: "Open Sans", sans-serif; }
  .person__name { font-size: 24px; font-weight: 300; color: var(--ink); line-height: 1.2; }
  .person__role { font-size: 9.5px; color: var(--ink-soft); margin-top: 12px; white-space: nowrap; }
  .card--back .rule { position: absolute; left: 0; right: 0; top: 98px; height: 3px; background: var(--green); }
  .contact { position: absolute; left: 24px; top: 160px; font-family: "Open Sans", sans-serif; font-size: 11.5px; color: var(--ink); line-height: 1.7; list-style: none; }
  .contact li { display: flex; align-items: center; gap: 7px; white-space: nowrap; }
  .contact svg { width: 11px; height: 11px; flex: none; }
  .offices { position: absolute; left: 24px; top: 232px; font-family: "Open Sans", sans-serif; font-size: 11.5px; color: var(--ink); line-height: 1.7; list-style: none; }
  .offices li { white-space: nowrap; }
</style>
</head>
<body>
<main class="stage">
  <section class="card card--front" aria-label="Card front">
    <h1 class="brand-name">Marlowe Bay Consulting</h1>
    <div class="rule"></div>
    <p class="tagline">So you can look forward to tomorrow<br>To helping you look forward to tomorrow</p>
    <p class="services">
      Relationships Counselling<span class="dot">•</span>Drug and Alcohol Counselling<br>
      Confidence Coaching<span class="dot">•</span>Life Coaching<span class="dot">•</span>Executive Coaching
    </p>
  </section>

  <section class="card card--back" aria-label="Card back">
    <h2 class="brand-name">Marlowe Bay Consulting</h2>
    <p class="tagline">So you can look forward to tomorrow<br>To helping you look forward to tomorrow</p>
    <div class="person">
      <p class="person__name">Tom Hadley</p>
      <p class="person__role">Clinical Psychotherapist and Executive Coach</p>
    </div>
    <div class="rule"></div>
    <ul class="contact">
      <li><svg viewBox="0 0 12 12" aria-hidden="true"><path d="M2 1h3l1 3-2 1a7 7 0 0 0 3 3l1-2 3 1v3c-6 0-9-3-9-9z" fill="#1f1f1f"/></svg>+612 9137 5264</li>
      <li><svg viewBox="0 0 12 12" aria-hidden="true"><rect x="0.5" y="2" width="11" height="8" fill="#1f1f1f"/><path d="M1 2.5l5 4 5-4" stroke="#fff" fill="none"/></svg>info@marlowebayconsulting.com.au</li>
      <li><svg viewBox="0 0 12 12" aria-hidden="true"><circle cx="6" cy="6" r="5.5" fill="#1f1f1f"/><path d="M0.5 6h11M6 .5v11M3 2c2 2 2 6 0 8M9 2c-2 2-2 6 0 8" stroke="#fff" stroke-width=".8" fill="none"/></svg>www.marlowebayconsulting.com.au</li>
    </ul>
    <ul class="offices">
      <li>Harbour Office: 48 Tallow Lane Glebe NSW 2037</li>
      <li>North Sydney Office: Suite 210 / 73 Linden Street North Sydney NSW 2060</li>
      <li>City Office: Suite 508 / 211 Carrow Street Sydney CBD NSW 2000</li>
    </ul>
  </section>
</main>
</body>
</html>
```